Business Card Design

I am a criminologist running a research and consultancy business on my own (RLConsultants)
I specialise in looking at fraud and other white-collar crimes. Also governance issues..
I would like a professional business card that would be appropriate both in the academic and business sector as I straddle both sectors. Normal shape - not square.
I am interested in seeing border Word Cloud type projects - black on white or white on black..
Example key words would be fraud, research, qualitative, interviews, quantitative, white-collar, reports, government, surveys, sample, governance, assurance, crime, offenders, prison etc (I can provide a full list if this is the option I go for). I also like Word Cloud borders as attached.
I am also interested in seeing other style business cards. Preferably one colour, plus black and white.
In particular I like black backgrounds with coloured words etc - colours like lime green are good.
I also like blues - especially teal if a traditional white background is chosen.
I don't have a logo - unless anyone can think of anything that's particularly appropriate.
Graphics can be used but they would be simple and stylish (dots, squares, lines, curves etc)
I would like the design to translate simply for a header for a website or blog.
My current website is www.penmarrow-dale.example but is out of date in terms of what I do and design.
I have attached a number of things that have caught my eye and inspired me.
I have asked for a one-sided business card in the first instance - however if someone comes up with a good cloud design that might go on one side, I would consider a two-sided one.
Design can be landscape or portrait.
Kind Regards
Liz
Industry/Entity Type
Landscape
Contact Information for Business Card
RLConsultants
Dr Hilary Penmarrow-Dale, MSc, BSc, **
42 Fernby Close
Brackwell, Ravenshire
QX27 4PL
+44(0)1632 960418
+44(0)7700 900582
www.penmarrow-dale.example
hilary@penmarrow-dale.example

```html
<!DOCTYPE html>
<html lang="en">
<head>
<meta charset="UTF-8">
<title>RLConsultants – Business Card</title>
<link rel="stylesheet" href="https://fonts.googleapis.com/css2?family=Lato:wght@400;700&family=Ubuntu:wght@700&display=swap">
<style>
  :root {
    --page-bg: #e6e4e1;
    --card-dark: #2f3032;
    --card-dark-edge: #26272a;
    --band-light: #ececec;
    --teal: #327c91;
    --teal-text: #3a87a0;
    --white: #ffffff;
    --muted: #d8dadc;
  }
  html, body {
    margin: 0;
    width: 1200px;
    height: 900px;
    overflow: hidden;
    background: var(--page-bg);
  }
  .card {
    position: absolute;
    left: 120px;
    top: 170px;
    width: 960px;
    height: 560px;
    background: var(--card-dark);
    overflow: hidden;
    box-shadow: 0 12px 30px rgba(0,0,0,0.18);
    font-family: "Lato", sans-serif;
    color: var(--white);
  }
  .card-texture {
    position: absolute;
    inset: 0;
    background: radial-gradient(ellipse at 60% 50%, #35363a 0%, var(--card-dark) 55%, var(--card-dark-edge) 100%);
  }
  .brand-band {
    position: absolute;
    left: 0;
    right: 0;
    top: 40px;
    height: 110px;
    background: var(--band-light);
  }
  .brand-name {
    position: absolute;
    right: 70px;
    top: 50%;
    transform: translateY(-52%);
    margin: 0;
    font-family: "Ubuntu", sans-serif;
    font-weight: 700;
    font-size: 62px;
    letter-spacing: 1px;
    color: var(--teal-text);
  }
  .person {
    position: absolute;
    left: 110px;
    top: 176px;
  }
  .person-name {
    margin: 0;
    font-family: "Ubuntu", sans-serif;
    font-weight: 700;
    font-size: 48px;
    letter-spacing: 1.5px;
    line-height: 1;
    padding-left: 18px;
  }
  .person-rule {
    width: 400px;
    height: 3px;
    background: var(--teal);
    margin-top: 14px;
  }
  .person-quals {
    text-align: right;
    width: 400px;
    margin-top: 6px;
    font-size: 18px;
    letter-spacing: 1.5px;
    color: var(--teal-text);
    font-weight: 700;
  }
  .contact-list {
    position: absolute;
    left: 128px;
    top: 290px;
    font-size: 21px;
    letter-spacing: 1px;
    line-height: 32px;
    color: var(--muted);
  }
  .contact-row {
    display: flex;
    align-items: flex-start;
    margin-bottom: 8px;
  }
  .contact-icon {
    width: 18px;
    height: 18px;
    margin-top: 7px;
    margin-right: 12px;
    flex: none;
    fill: var(--teal-text);
  }
  .footer-band-left {
    position: absolute;
    left: 0;
    bottom: 0;
    width: 480px;
    height: 106px;
    background: var(--teal);
  }
  .footer-band-full {
    position: absolute;
    left: 0;
    right: 0;
    bottom: 0;
    height: 52px;
    background: var(--teal);
  }
  .footer-email, .footer-web {
    position: absolute;
    display: flex;
    align-items: center;
    font-size: 21px;
    letter-spacing: 1px;
    line-height: 28px;
    color: var(--white);
  }
  .footer-email { left: 110px; bottom: 62px; }
  .footer-web { right: 70px; bottom: 12px; }
  .footer-email .contact-icon, .footer-web .contact-icon {
    fill: var(--white);
    margin-top: 0;
  }
</style>
</head>
<body>
  <div class="card">
    <div class="card-texture" role="img" aria-label="Fine grid texture on charcoal background"></div>

    <div class="brand-band">
      <h1 class="brand-name">RLConsultants</h1>
    </div>

    <div class="person">
      <h2 class="person-name">Dr Hilary</h2>
      <div class="person-rule"></div>
      <div class="person-quals">MSc, BSc</div>
    </div>

    <div class="contact-list">
      <div class="contact-row">
        <svg class="contact-icon" viewBox="0 0 24 24" aria-hidden="true"><path d="M6.6 10.8a15.5 15.5 0 0 0 6.6 6.6l2.2-2.2c.3-.3.7-.4 1-.2 1.1.4 2.3.6 3.6.6.6 0 1 .4 1 1V20c0 .6-.4 1-1 1A17 17 0 0 1 3 4c0-.6.4-1 1-1h3.5c.6 0 1 .4 1 1 0 1.3.2 2.5.6 3.6.1.3 0 .7-.2 1z"/></svg>
        <div>+44(0)1632 960418<br>+44(0)7700 900582</div>
      </div>
      <div class="contact-row">
        <svg class="contact-icon" viewBox="0 0 24 24" aria-hidden="true"><path d="M12 2a7 7 0 0 0-7 7c0 5.2 7 13 7 13s7-7.8 7-13a7 7 0 0 0-7-7zm0 9.5A2.5 2.5 0 1 1 12 6.5a2.5 2.5 0 0 1 0 5z"/></svg>
        <div>42 Fernby Close Brackwell,<br>Ravenshire QX27 4PL</div>
      </div>
    </div>

    <div class="footer-band-left"></div>
    <div class="footer-band-full"></div>

    <div class="footer-email">
      <svg class="contact-icon" viewBox="0 0 24 24" aria-hidden="true"><path d="M3 5h18v2l-9 6-9-6zM3 9l9 6 9-6v10H3z"/></svg>
      hilary@penmarrow-dale.example
    </div>

    <div class="footer-web">
      <svg class="contact-icon" viewBox="0 0 24 24" aria-hidden="true"><circle cx="12" cy="12" r="9" fill="none" stroke="#fff" stroke-width="2"/><ellipse cx="12" cy="12" rx="4" ry="9" fill="none" stroke="#fff" stroke-width="1.6"/><path d="M3 12h18M5 7.5h14M5 16.5h14" stroke="#fff" stroke-width="1.4"/></svg>
      www.penmarrow-dale.example
    </div>
  </div>
</body>
</html>
```